Restoration Specialist in need of business card designs

One side of the business card is a bathroom ripped out down to the studs with just a sink and toilet and then the other side is the bathroom (same sink and toilet) but put back together. Like a before and after on each side behind our information. Stand out, hard to forget, business cards for my restoration company. I want a unique concept all together.
Must include in no particular order:
our business name "Keystone Renewals"
Possible Logo for a restoration company
Owner; Martin Velasko
410-555-0192
mvelasko@keystonerenewalsMD.example
KeystoneRenewalsMD.example (our company website) BUT I am open to any and all designs and options.

Target Market(s)

Customers, Men in the mitigation, plumbing, electrical, HVAC, Roofing, insurance companies

Industry/Entity Type

Restoration/ construction

Contact Information for Business Card

Must include in no particular order: our business name "Keystone Renewals" Owner; Martin Velasko 410-555-0192 mvelasko@keystonerenewalsMD.example KeystoneRenewalsMD.example (our company website) MAY include a list of our services: Residential~ Emergency Response ~ Board- up~ Complete Restoration

Font styles to use
Serif

Colors
0054AA
0677BA
7BADD7
CADEEF
E8F1F8
F0912C
F2A743
F7CA91
FBE8D2
FDF5EE

Requirements
Must have
• unique, memorable, not something men have seen over and over again,
Nice to have
• eye catching
Should not have
• Been something I could have made by myself

```html
<!DOCTYPE html>
<html lang="en">
<head>
<meta charset="utf-8">
<title>Keystone Renewals – Business Cards</title>
<link rel="stylesheet" href="https://fonts.googleapis.com/css2?family=Tinos:wght@400;700&display=swap">
<style>
  :root {
    --page: #d9dadc;
    --navy: #11243a;
    --orange: #f0912c;
    --white: #ffffff;
  }
  * { box-sizing: border-box; margin: 0; padding: 0; }
  html, body { width: 1200px; height: 880px; overflow: hidden; }
  body {
    background: var(--page);
    font-family: "Tinos", "Times New Roman", serif;
    position: relative;
  }
  .card {
    position: absolute;
    left: 240px;
    width: 720px;
    height: 400px;
    background: var(--navy);
    border-radius: 22px;
    color: var(--white);
    overflow: hidden;
  }
  .card--back { top: 24px; }
  .card--front {
    top: 446px;
    overflow: visible;
    box-shadow: 0 8px 0 var(--orange);
  }
  .brand {
    position: absolute;
    left: 0; right: 0;
    display: flex;
    justify-content: center;
    align-items: center;
    gap: 14px;
  }
  .brand__mark {
    width: 26px; height: 26px;
    background: var(--orange);
  }
  .brand__name {
    font-weight: 700;
    font-size: 46px;
    color: var(--orange);
    letter-spacing: 0.5px;
    white-space: nowrap;
  }
  .card--back .brand { top: 96px; }
  .card--front .brand { top: 70px; }

  .services {
    position: absolute;
    top: 200px; left: 0; right: 0;
    text-align: center;
  }
  .services__title {
    font-weight: 700;
    font-size: 24px;
    color: var(--orange);
    letter-spacing: 0.5px;
    margin-bottom: 10px;
  }
  .services__list {
    font-size: 23px;
    line-height: 1.3;
  }

  .owner {
    position: absolute;
    left: 36px;
    top: 262px;
    width: 244px;
    text-align: right;
  }
  .owner__name {
    font-weight: 700;
    font-size: 36px;
    color: var(--orange);
    line-height: 1.1;
    white-space: nowrap;
  }
  .owner__role { font-size: 21px; }

  .divider {
    position: absolute;
    left: 302px;
    top: 220px;
    width: 1px;
    height: 110px;
    background: var(--orange);
  }

  .contact {
    position: absolute;
    left: 326px;
    top: 222px;
    list-style: none;
  }
  .contact__item {
    display: flex;
    align-items: center;
    gap: 10px;
    font-size: 19px;
    height: 34px;
    white-space: nowrap;
  }
  .contact__icon { width: 20px; height: 20px; flex: none; }
</style>
</head>
<body>

  <section class="card card--back">
    <div class="brand">
      <span class="brand__mark"></span>
      <span class="brand__name">Keystone Renewals</span>
    </div>
    <div class="services">
      <p class="services__title">OUR SERVICES</p>
      <p class="services__list">Residential • Emergency Response • Board- up<br>• Storm Protection • Complete Restoration</p>
    </div>
  </section>

  <section class="card card--front">
    <div class="brand">
      <span class="brand__mark"></span>
      <span class="brand__name">Keystone Renewals</span>
    </div>

    <div class="owner">
      <p class="owner__name">Martin Velasko</p>
      <p class="owner__role">Owner</p>
    </div>

    <div class="divider"></div>

    <ul class="contact">
      <li class="contact__item">
        <svg class="contact__icon" viewBox="0 0 24 24" aria-hidden="true"><path fill="#f0912c" d="M6.6 10.8a15 15 0 0 0 6.6 6.6l2.2-2.2c.3-.3.7-.4 1-.2 1.1.4 2.3.6 3.6.6.6 0 1 .4 1 1V20c0 .6-.4 1-1 1A17 17 0 0 1 3 4c0-.6.4-1 1-1h3.5c.6 0 1 .4 1 1 0 1.3.2 2.5.6 3.6.1.3 0 .7-.2 1z"/></svg>
        <span>410-555-0192</span>
      </li>
      <li class="contact__item">
        <svg class="contact__icon" viewBox="0 0 24 24" aria-hidden="true"><path fill="#f0912c" d="M2 5h20v14H2z"/><path fill="none" stroke="#11243a" stroke-width="1.8" d="M2.5 5.5 12 13l9.5-7.5"/></svg>
        <span>mvelasko@keystonerenewalsMD.example</span>
      </li>
      <li class="contact__item">
        <svg class="contact__icon" viewBox="0 0 24 24" aria-hidden="true"><g fill="none" stroke="#f0912c" stroke-width="2"><circle cx="12" cy="12" r="9.5"/><ellipse cx="12" cy="12" rx="4" ry="9.5"/><path d="M2.5 12h19"/></g></svg>
        <span>KeystoneRenewalsMD.example</span>
      </li>
    </ul>
  </section>

</body>
</html>
```